marla verstegen
chef
marla verstegen - Chef / Catering
Creative Brief
Use specific fonts
may mix logo font with another font, both must be free and downloadable
Simple
professional chef
none
marla@marlaverstegen.net
marlaverstegen.net
For the biz cards: on the flip side, my social media info: website: marlaverstegen.net twitter: @marlaverstegen facebook: facebook.com/marla.verstegen blog: www.ourfinaldinnertable.net I'd like to have the symbols rather than words for social media I would like to have a folded card for thank yous and notes on the back of the envelope place the logo, then underneath: 518 tuckaway st. denver, co 80219 I would like the theme of the stars in the logo to be pulled through the products
website: marlaverstegen.net twitter: @marlaverstegen facebook: facebook.com/marla.verstegen blog: ourfinaldinnertable.net

```html
<!DOCTYPE html>
<html lang="en">
<head>
<meta charset="utf-8">
<title>marla verstegen — business card</title>
<link rel="stylesheet" href="https://fonts.googleapis.com/css2?family=Open+Sans:wght@400;700&display=swap">
<style>
  :root {
    --backdrop: #e9e4de;
    --card-white: #ffffff;
    --chef-red: #b3312b;
    --divider: #d9d4cf;
    --tagline-grey: #8a8a8a;
    --on-red: #ffffff;
  }
  * { margin: 0; padding: 0; box-sizing: border-box; }
  html, body {
    width: 1200px; height: 780px; overflow: hidden;
    background: var(--backdrop);
    font-family: "Open Sans", sans-serif;
  }
  .card {
    position: absolute; left: 100px; top: 104px;
    width: 1000px; height: 572px;
    border-radius: 34px; overflow: hidden;
    display: flex;
    box-shadow: 0 10px 30px rgba(0,0,0,0.18);
  }
  .card-front {
    width: 440px; height: 100%;
    background: var(--card-white);
    border-right: 4px solid var(--divider);
    display: flex; align-items: center; justify-content: center;
    padding-top: 60px;
  }
  .logo-lockup {
    display: flex; flex-direction: column; align-items: flex-end;
  }
  .logo-name {
    font-weight: 400; font-size: 40px;
    color: var(--chef-red); line-height: 1.1;
  }
  .logo-tagline {
    margin-top: 4px;
    font-size: 16px;
    color: var(--tagline-grey); letter-spacing: 0.5px;
  }
  .logo-tagline .bullet { color: var(--chef-red); }
  .card-details {
    flex: 1; background: var(--chef-red); color: var(--on-red);
    position: relative;
  }
  .details-header {
    position: absolute; top: 40px; right: 44px; text-align: right;
    font-weight: 700; line-height: 1.2;
  }
  .details-name { font-size: 30px; }
  .details-title { font-size: 22px; }
  .contact-list {
    position: absolute; right: 40px; bottom: 70px;
    list-style: none; text-align: right;
    font-size: 20px;
  }
  .contact-list li {
    display: flex; justify-content: flex-end; align-items: center;
    gap: 12px; height: 36px;
  }
  .contact-icon { width: 22px; height: 22px; flex: none; }
</style>
</head>
<body>
  <div class="card">
    <section class="card-front">
      <div class="logo-lockup">
        <div class="logo-name">marla verstegen</div>
        <div class="logo-tagline"><span class="bullet">•</span>professional chef<span class="bullet">•</span></div>
      </div>
    </section>
    <section class="card-details">
      <header class="details-header">
        <div class="details-name">marla verstegen</div>
        <div class="details-title">professional chef</div>
      </header>
      <ul class="contact-list">
        <li>303.555.0142
          <svg class="contact-icon" viewBox="0 0 24 24" aria-label="phone">
            <path d="M6.6 3.5c.6-.4 1.4-.3 1.8.3l2 3c.4.6.3 1.3-.2 1.7l-1.4 1.1c.9 2 2.6 3.8 4.6 4.7l1.1-1.4c.4-.5 1.2-.6 1.7-.2l3 2c.6.4.7 1.2.3 1.8l-1.3 1.9c-.6.9-1.7 1.3-2.7 1C9.7 18.3 5.7 14.3 4.6 8.5c-.2-1 .2-2 1-2.6z" fill="var(--on-red)"/>
          </svg>
        </li>
        <li>marla@marlaverstegen.net
          <svg class="contact-icon" viewBox="0 0 24 24" aria-label="email">
            <circle cx="12" cy="12" r="4" fill="none" stroke="var(--on-red)" stroke-width="2.4"/>
            <path d="M16 8v5.5c0 1.5 1 2.5 2.3 2.5S21 15 21 12a9 9 0 1 0-3.6 7.2" fill="none" stroke="var(--on-red)" stroke-width="2.4" stroke-linecap="round"/>
          </svg>
        </li>
        <li>marlaverstegen.net
          <svg class="contact-icon" viewBox="0 0 24 24" aria-label="website">
            <circle cx="12" cy="12" r="9" fill="none" stroke="var(--on-red)" stroke-width="2"/>
            <ellipse cx="12" cy="12" rx="4" ry="9" fill="none" stroke="var(--on-red)" stroke-width="1.6"/>
            <path d="M3 12h18M5 7h14M5 17h14" stroke="var(--on-red)" stroke-width="1.4"/>
          </svg>
        </li>
      </ul>
    </section>
  </div>
</body>
</html>
```